Harbor Crew Biz Cards

looking for a new catchy business card where my cell number is very prominent:
My pic and logo are attached. My whole picture isn't necessary if it makes more sense to crop it.

Info needed:

(Big) Marcus Pellow
(Medium) Real Estate Professional
(Medium) Buyer/Seller Specialist
(Big) Call/Text 410-738-2914
(small) Marcuspell@quillbox.com
(small) www.harborcrewlists.com

(very small)
The Harbor Crew
at Keystead Real Estate
2457 W Tanbrook Rd, Bel Air, MD 21014
833-555-2690

```html
<!DOCTYPE html>
<html lang="en">
<head>
<meta charset="utf-8">
<title>Harbor Crew Business Cards</title>
<link href="https://fonts.googleapis.com/css2?family=Montserrat:wght@400;500;600;700&display=swap" rel="stylesheet">
<style>
  :root {
    --navy: #0f2d5c;
    --navy-light: #1c3f73;
    --silver: #a3a3a3;
    --white: #ffffff;
    --backdrop: #3a3a3a;
  }
  * { box-sizing: border-box; margin: 0; padding: 0; }
  html, body { width: 1200px; height: 1200px; overflow: hidden; }
  body {
    background: var(--backdrop);
    font-family: "Montserrat", sans-serif;
    display: flex;
    flex-direction: column;
    align-items: center;
    justify-content: center;
    gap: 50px;
  }
  .card {
    position: relative;
    width: 860px;
    height: 491px;
    border-radius: 34px;
    overflow: hidden;
  }
  .card-front { background: var(--white); }
  .front-shapes { position: absolute; inset: 0; }
  .portrait {
    position: absolute;
    left: 660px;
    top: 44px;
    width: 170px;
    height: 447px;
    background: linear-gradient(180deg, #e9ebef 0%, #4a5568 35%, #3b4456 100%);
    border-radius: 85px 85px 0 0;
    opacity: 0.85;
  }
  .details {
    position: absolute;
    left: 52px;
    top: 60px;
    color: var(--white);
  }
  .agent-name {
    font-size: 38px;
    font-weight: 700;
    color: var(--silver);
    letter-spacing: 0.3px;
    text-transform: uppercase;
    line-height: 1;
    white-space: nowrap;
  }
  .agent-role {
    font-size: 18px;
    font-weight: 500;
    text-transform: uppercase;
    line-height: 1.15;
    margin-top: 8px;
  }
  .phone-block {
    display: flex;
    align-items: flex-end;
    gap: 12px;
    margin-top: 24px;
  }
  .phone-label { font-size: 23px; font-weight: 700; line-height: 1; }
  .phone-number { font-size: 40px; font-weight: 700; line-height: 1.05; white-space: nowrap; }
  .contact-line {
    display: flex;
    align-items: center;
    gap: 14px;
    font-size: 20px;
    font-weight: 500;
    margin-top: 12px;
    white-space: nowrap;
  }
  .icon { width: 28px; height: 28px; flex: none; }
  .office {
    margin-top: 24px;
    font-size: 15px;
    font-weight: 500;
    line-height: 1.3;
    white-space: nowrap;
  }
  .office-team { color: var(--silver); }

  .card-back {
    background: linear-gradient(115deg, var(--navy) 0%, var(--navy) 55%, var(--navy-light) 70%, var(--navy) 85%);
    display: flex;
    align-items: center;
    justify-content: center;
    gap: 22px;
  }
  .brand-dot {
    width: 46px;
    height: 46px;
    border-radius: 50%;
    background: var(--silver);
  }
  .brand-name {
    font-size: 52px;
    font-weight: 600;
    color: var(--white);
    text-transform: uppercase;
    letter-spacing: 3px;
  }
</style>
</head>
<body>
  <section class="card card-front">
    <svg class="front-shapes" viewBox="0 0 860 491" width="860" height="491" aria-hidden="true">
      <path d="M0 0 H466 C596 80 646 300 616 491 H0 Z" fill="var(--silver)"/>
      <path d="M0 0 H450 C580 80 630 300 600 491 H0 Z" fill="var(--white)"/>
      <path d="M0 0 H430 C560 80 610 300 580 491 H0 Z" fill="var(--navy)"/>
    </svg>
    <div class="portrait" role="img" aria-label="Portrait photo of the agent in a dark blazer"></div>
    <div class="details">
      <h1 class="agent-name">Marcus Pellow</h1>
      <p class="agent-role">Real Estate Professional<br>Buyer/Seller Specialist</p>
      <div class="phone-block">
        <svg class="icon" viewBox="0 0 24 24" aria-hidden="true"><path fill="var(--silver)" d="M6.6 10.8a15.1 15.1 0 0 0 6.6 6.6l2.2-2.2a1 1 0 0 1 1-.25 11.4 11.4 0 0 0 3.6.57 1 1 0 0 1 1 1V20a1 1 0 0 1-1 1A17 17 0 0 1 3 4a1 1 0 0 1 1-1h3.5a1 1 0 0 1 1 1c0 1.25.2 2.45.57 3.6a1 1 0 0 1-.25 1z"/></svg>
        <div>
          <p class="phone-label">Call/Text</p>
          <p class="phone-number">410-738-2914</p>
        </div>
      </div>
      <p class="contact-line">
        <svg class="icon" viewBox="0 0 24 24" aria-hidden="true"><rect x="2" y="5" width="20" height="14" rx="1" fill="var(--silver)"/><path d="M2 6l10 7 10-7" fill="none" stroke="var(--navy)" stroke-width="1.6"/></svg>
        Marcuspell@quillbox.com
      </p>
      <p class="contact-line">
        <svg class="icon" viewBox="0 0 24 24" aria-hidden="true"><g fill="none" stroke="var(--silver)" stroke-width="1.6"><circle cx="12" cy="12" r="9.5"/><ellipse cx="12" cy="12" rx="4" ry="9.5"/><path d="M2.5 12h19M4 7h16M4 17h16"/></g></svg>
        www.harborcrewlists.com
      </p>
      <div class="office">
        <p class="office-team">The Harbor Crew</p>
        <p>at Keystead Real Estate</p>
        <p>2457 W Tanbrook Rd, Bel Air, MD 21014</p>
        <p>833-555-2690</p>
      </div>
    </div>
  </section>

  <section class="card card-back">
    <span class="brand-dot" aria-hidden="true"></span>
    <p class="brand-name">The Harbor Crew</p>
  </section>
</body>
</html>
```